Webdesign für Ein traditionsreicher & moderner Handwerksbetrieb
Zielgruppe
Werbeagentur sucht Designer für Handwerker-Website
Aufgabenstellung
Es wird ein frisches, innovatives Design benötigt, das das Dachdeckerhandwerk adäquat repräsentiert. Außerdem soll es eine gewisse Kapazität, Professionalität und Seriosität widerspiegeln.

```html
<!DOCTYPE html>
<html lang="de">
<head>
<meta charset="utf-8">
<title>Dachdeckerei – Alles rund ums Dach</title>
<link href="https://fonts.googleapis.com/css2?family=Montserrat:wght@400;500;600;700&display=swap" rel="stylesheet">
<style>
:root{
  --brick:#b5472c;
  --charcoal:#2a2d2b;
  --ink:#2b2b2b;
  --placeholder:#d9d9d9;
  --white:#ffffff;
  --rule:#e2e2e2;
}
*{margin:0;padding:0;box-sizing:border-box}
html,body{width:1200px;height:2491px;overflow:hidden;background:var(--white)}
body{position:relative;font-family:"Montserrat",Arial,sans-serif;color:var(--ink)}
.abs{position:absolute}

/* Header */
.hero{left:0;top:108px;width:1200px;height:682px;
  background:linear-gradient(180deg,#4c6a9a 0%,#8a9dbb 30%,#b3bccb 55%,#a9b0bb 80%,#c98a63 93%,#a8553a 100%)}
.logo-box{left:112px;top:28px;width:225px;height:100px;background:var(--charcoal);
  color:var(--white);font-size:38px;font-weight:500;display:flex;align-items:center;justify-content:center;letter-spacing:-1px}
.main-nav{left:363px;top:28px;display:flex;gap:9px}
.main-nav a{width:138px;height:100px;background:var(--brick);color:var(--white);text-decoration:none;
  font-size:15px;font-weight:600;display:flex;align-items:center;justify-content:center}
.hero-title{left:112px;top:404px;color:var(--white)}
.hero-title .lead{font-size:38px;font-weight:400;line-height:46px;letter-spacing:.5px}
.hero-title .strong{font-size:38px;font-weight:700;line-height:46px;display:inline-block;border-bottom:3px solid var(--white);padding-bottom:2px}

/* Services */
.services-band{left:0;top:790px;width:1200px;height:430px;background:var(--brick)}
.service{top:743px;width:308px;text-align:center;color:var(--white)}
.service .thumb{width:308px;height:206px;background:var(--placeholder);border:1px solid #bbb}
.service h3{margin-top:19px;font-size:31px;font-weight:500;line-height:36px;letter-spacing:.5px}
.service p{margin-top:11px;font-size:10.5px;line-height:18.4px;padding:0 10px}
.service .btn-light{display:inline-block;margin-top:21px;width:171px;height:49px;line-height:49px;background:var(--white);
  color:var(--ink);font-size:16px;font-weight:500}

/* Section headings */
.section-title{left:0;width:1200px;text-align:center;font-size:30px;font-weight:500;letter-spacing:.5px}
.section-title span{color:var(--brick)}

.intro{left:112px;top:1337px;width:490px}
.intro .claim{color:var(--brick);font-size:15px;line-height:25px;font-weight:500}
.intro .body{margin-top:8px;font-size:10.5px;line-height:18.4px}
.btn-solid{background:var(--brick);color:var(--white);font-size:16px;font-weight:500;height:49px;line-height:49px;text-align:center}
.checklist{left:616px;top:1335px;list-style:none}
.checklist li{display:flex;align-items:center;height:40px;font-size:15px;font-weight:500}
.checklist svg{width:17px;height:14px;margin-right:16px}
.divider{left:112px;top:1653px;width:976px;height:1px;background:var(--rule)}

/* References */
.ref{top:1775px;width:225px}
.ref .thumb{width:225px;height:152px;background:var(--placeholder)}
.ref h4{margin-top:24px;color:var(--brick);font-size:14.5px;font-weight:700;line-height:19px}
.ref p{margin-top:16px;font-size:10.5px;line-height:18.4px}

/* Footer */
.site-footer{left:0;top:2230px;width:1200px;height:261px;background:var(--charcoal);color:var(--white)}
.footer-logo{left:114px;top:52px;font-size:38px;font-weight:500;letter-spacing:-1px}
.footer-nav{left:446px;top:45px;display:flex;gap:19px;font-size:15px;font-weight:600}
.footer-text{left:446px;top:89px;width:636px;font-size:10.3px;line-height:18.4px}
</style>
</head>
<body>

<div class="abs hero" role="img" aria-label="Dachdecker in grünem Shirt fängt einen geworfenen Dachziegel vor bewölktem Himmel auf dem Dach"></div>
<div class="abs logo-box">LOGO</div>
<nav class="abs main-nav">
  <a href="#">LEISTUNGEN</a><a href="#">ÜBER UNS</a><a href="#">REFERENZEN</a><a href="#">NEWS</a><a href="#">KONTAKT</a>
</nav>
<div class="abs hero-title">
  <div class="lead">SEIT ÜBER 65 JAHREN</div>
  <div class="strong">ALLES RUND UMS DACH</div>
</div>

<div class="abs services-band"></div>
<div class="abs service" style="left:112px">
  <div class="thumb" role="img" aria-label="Foto Dachreparatur"></div>
  <h3>DACH<br>REPERATUR</h3>
  <p>As a protective element of any building roof may require some repair if it's not treated properly for a long time. Nevertheless, our specialists know what</p>
  <span class="btn-light">MEHR ERFAHREN</span>
</div>
<div class="abs service" style="left:446px">
  <div class="thumb" role="img" aria-label="Foto Dachinstandhaltung"></div>
  <h3>DACH<br>INSTANDHALTUNG</h3>
  <p>As a protective element of any building roof may require some repair if it's not treated properly for a long time. Nevertheless, our specialists know what</p>
  <span class="btn-light">MEHR ERFAHREN</span>
</div>
<div class="abs service" style="left:779px">
  <div class="thumb" role="img" aria-label="Foto Dachrinnenreinigung"></div>
  <h3>DACHRINNEN<br>REINIGUNG</h3>
  <p>Eavestroughs are important elements of any building. They protect your house from excessive water, but also require seasonal cleaning every fall. These elements help your house</p>
  <span class="btn-light">MEHR ERFAHREN</span>
</div>

<h2 class="abs section-title" style="top:1262px">WIR SCHAFFEN <span>JEDES DACH</span></h2>
<div class="abs intro">
  <p class="claim">IT IS ESTIMATED THAT 70% OF ROOFS ARE REPLACED WITH 30% OR MORE OF THEIR SERVICEABLE LIFE STILL REMAINING. THAT COULD MEAN HUNDREDS OF THOUSANDS OF DOLLARS WASTED.</p>
  <p class="body">If only you could identify and correct potential roofing problems before it's too late. With our company plans, you can! We're proven experts in roof resolution solutions and are highly skilled at uncovering all the commercial roof threats that could cause deterioration, malfunction and even collapse. With our preventive maintenance plan, we can typically double the life span of a commercial roof.</p>
</div>
<div class="abs btn-solid" style="left:112px;top:1552px;width:171px">MEHR ERFAHREN</div>
<ul class="abs checklist">
  <li><svg viewBox="0 0 17 14"><path d="M1.5 7.5l4.5 4.5L15.5 2" fill="none" stroke="#b5472c" stroke-width="3"/></svg>STEILDACH</li>
  <li><svg viewBox="0 0 17 14"><path d="M1.5 7.5l4.5 4.5L15.5 2" fill="none" stroke="#b5472c" stroke-width="3"/></svg>FLACHDACH</li>
  <li><svg viewBox="0 0 17 14"><path d="M1.5 7.5l4.5 4.5L15.5 2" fill="none" stroke="#b5472c" stroke-width="3"/></svg>DACHFENSTER</li>
  <li><svg viewBox="0 0 17 14"><path d="M1.5 7.5l4.5 4.5L15.5 2" fill="none" stroke="#b5472c" stroke-width="3"/></svg>BALKONABDICHTUNG</li>
  <li><svg viewBox="0 0 17 14"><path d="M1.5 7.5l4.5 4.5L15.5 2" fill="none" stroke="#b5472c" stroke-width="3"/></svg>KAMINE</li>
  <li><svg viewBox="0 0 17 14"><path d="M1.5 7.5l4.5 4.5L15.5 2" fill="none" stroke="#b5472c" stroke-width="3"/></svg>DACHBEGRÜNUNG</li>
  <li><svg viewBox="0 0 17 14"><path d="M1.5 7.5l4.5 4.5L15.5 2" fill="none" stroke="#b5472c" stroke-width="3"/></svg>FASSADENBEKLEIDUNG</li>
</ul>
<div class="abs divider"></div>

<h2 class="abs section-title" style="top:1693px">UNSERE <span>REFERENZEN</span></h2>
<article class="abs ref" style="left:112px">
  <div class="thumb" role="img" aria-label="Referenzfoto Dachwartung"></div>
  <h4>PREVENTATIVE ROOF MAINTENANCE</h4>
  <p>Maintaining your roof is a vital process in a lifecycle of your house. If you want your roof to stay functional, preventative maintenance should be</p>
</article>
<article class="abs ref" style="left:362px">
  <div class="thumb" role="img" aria-label="Referenzfoto Dachreparatur"></div>
  <h4>ROOF REPAIR VS. ROOF REPLACEMENT</h4>
  <p>These two options are what house owners run into sooner or later. Thus, it is always useful to know what you may encounter before it</p>
</article>
<article class="abs ref" style="left:612px">
  <div class="thumb" role="img" aria-label="Referenzfoto Gewerbedach"></div>
  <h4>MERGENCY COMMERCIAL ROOF REPAIR</h4>
  <p>If you accidentally happened to be one of those house owners who need an urgent roof repair service, then this service may be just what</p>
</article>
<article class="abs ref" style="left:863px">
  <div class="thumb" role="img" aria-label="Referenzfoto Flachdach"></div>
  <h4>FLAT ROOF REPAIRS FOR PROJECTS OF ANY SIZE</h4>
  <p>Office buildings and entertainment centers are those types of buildings that often require some roof repair if they are not treated properly.</p>
</article>
<div class="abs btn-solid" style="left:504px;top:2105px;width:191px">ALLE REFERENZEN</div>

<footer class="abs site-footer">
  <div class="abs footer-logo">LOGO</div>
  <nav class="abs footer-nav"><span>START</span><span>LEISTUNGEN</span><span>ÜBER UNS</span><span>REFERENZEN</span><span>NEWS</span><span>KONTAKT</span></nav>
  <p class="abs footer-text">For over 40 years, our company has provided expert roofing services to residential and commercial property owners in the area. We are proud to say that we have more than 100 installations to our credit. That's a lot of happy customers. Manufacturer product knowledge training, uniform installation standards, continuous safety training and a determined commitment to 100% customer satisfaction are the hallmarks of our service. With us you'll have peace of mind knowing your property is in expert hands. And yes, our expert services are affordable. Take advantage of our payment options to match your financial comfort.</p>
</footer>

</body>
</html>
```